Visitenkarte erstellen für Reiki Praxis

Visitenkarten für Reiki Praxis Doppelseitig

business cards reiki practice double-sided

The background can also be a different color

```html
<!DOCTYPE html>
<html lang="de">
<head>
<meta charset="utf-8">
<title>Stille Quelle – Visitenkarte</title>
<link rel="stylesheet" href="https://fonts.googleapis.com/css2?family=Jost:wght@300;400&display=swap">
<style>
  :root {
    --page: #e6e7e9;
    --card: #141414;
    --white: #f2f2f2;
    --gold: #c99a55;
    --rose: #b8648f;
    --peach: #f4a06a;
    --sage: #a9a593;
    --faint: #2a2727;
  }
  * { margin: 0; padding: 0; box-sizing: border-box; }
  html, body { width: 1200px; height: 1200px; overflow: hidden; }
  body {
    background: var(--page);
    font-family: "Jost", sans-serif;
    position: relative;
  }
  .card {
    position: absolute;
    left: 198px;
    width: 804px;
    height: 520px;
    background: var(--card);
    overflow: hidden;
  }
  .card--front { top: 70px; }
  .card--back { top: 624px; }

  .front-name {
    position: absolute;
    left: 0; right: 0;
    top: 228px;
    text-align: center;
    font-size: 58px;
    font-weight: 300;
    letter-spacing: 6px;
    color: var(--gold);
  }

  .back-decor {
    position: absolute;
    left: 470px;
    top: 90px;
    width: 440px;
    height: 440px;
    border-radius: 50%;
    border: 3px solid var(--faint);
  }

  .brand-dot {
    position: absolute;
    left: 203px;
    top: 78px;
    width: 36px;
    height: 36px;
    border-radius: 50%;
    border: 2px solid var(--gold);
  }
  .brand-name {
    position: absolute;
    left: 70px;
    width: 302px;
    top: 146px;
    text-align: center;
    font-size: 29px;
    font-weight: 400;
    letter-spacing: 1px;
    color: var(--white);
  }

  .person-name {
    position: absolute;
    left: 72px;
    top: 236px;
    font-size: 30px;
    font-weight: 400;
    letter-spacing: 1px;
    background: linear-gradient(90deg, var(--rose), var(--peach));
    -webkit-background-clip: text;
    background-clip: text;
    color: transparent;
  }
  .person-role {
    position: absolute;
    left: 72px;
    top: 278px;
    font-size: 22px;
    font-weight: 400;
    color: var(--white);
  }

  .contact-list { list-style: none; position: absolute; left: 72px; top: 338px; }
  .contact-item {
    display: flex;
    align-items: center;
    height: 36.7px;
    font-size: 21px;
    font-weight: 300;
    color: var(--white);
    letter-spacing: 0.3px;
  }
  .contact-icon { width: 26px; height: 26px; margin-right: 17px; flex: none; }
</style>
</head>
<body>
  <svg width="0" height="0" style="position:absolute">
    <defs>
      <linearGradient id="icon-grad" x1="0" y1="0" x2="1" y2="1">
        <stop offset="0" stop-color="#b8648f"/>
        <stop offset="1" stop-color="#f4a06a"/>
      </linearGradient>
    </defs>
  </svg>

  <section class="card card--front">
    <p class="front-name">STILLE QUELLE</p>
  </section>

  <section class="card card--back">
    <div class="back-decor"></div>

    <div class="brand-dot"></div>
    <p class="brand-name">STILLE QUELLE</p>

    <p class="person-name">MARA LINDT</p>
    <p class="person-role">Eigentümer</p>

    <ul class="contact-list">
      <li class="contact-item">
        <svg class="contact-icon" viewBox="0 0 24 24"><path fill="url(#icon-grad)" d="M6.6 2.5c.6-.4 1.4-.3 1.8.3l2.3 3.3c.4.6.3 1.3-.2 1.8l-1.4 1.3c.9 2.1 2.6 3.9 4.7 5l1.4-1.3c.5-.5 1.3-.5 1.8-.1l3.2 2.4c.6.4.7 1.3.2 1.9l-1.5 1.9c-.8 1-2.2 1.3-3.4.8C9 17.4 5.1 13.3 3 7.4c-.4-1.1 0-2.4 1-3.1z"/></svg>
        123456789
      </li>
      <li class="contact-item">
        <svg class="contact-icon" viewBox="0 0 24 24"><rect x="2" y="5" width="20" height="14" fill="url(#icon-grad)"/><path d="M2.5 5.5 12 13l9.5-7.5M2.5 18.5l7-6M21.5 18.5l-7-6" fill="none" stroke="#141414" stroke-width="1.4"/></svg>
        kontakt@stillequelle.de
      </li>
      <li class="contact-item">
        <svg class="contact-icon" viewBox="0 0 24 24" fill="none" stroke="url(#icon-grad)" stroke-width="1.6"><circle cx="12" cy="12" r="9.5"/><ellipse cx="12" cy="12" rx="4.2" ry="9.5"/><path d="M2.5 12h19M4 7h16M4 17h16M12 2.5v19"/></svg>
        www.stillequelle.de
      </li>
      <li class="contact-item">
        <svg class="contact-icon" viewBox="0 0 24 24"><path fill="url(#icon-grad)" d="M12 1.5c-4 0-7 3-7 7 0 5 7 14 7 14s7-9 7-14c0-4-3-7-7-7zm0 10a3 3 0 1 1 0-6 3 3 0 0 1 0 6z"/></svg>
        Name Ihrer Region, Stadt, Deutschland 12345
      </li>
    </ul>
  </section>
</body>
</html>
```